To revamp the exting web page and Company presentation to new propsective client

We are company establish in 2006. We have a combine of Veltrix implementation team of more than 10 years. We focus on the following areas

a) Veltrix T-ledger range implementation
b) Veltrix T-ledger range platform migration
c) Large database size in excess of 20TB

We need to redesign a our existing new card to give a new look and refresh look. Kindly visit our website for more info www.bnlzq.com

Your main them is blue color and hope to hear from you all.

Target Market(s)

Professional clients

Industry/Entity Type

Information Technology

Contact Information for Business Card

To market our as the leading Veltrix partner in Veltrix t-ledger range implementation

Number of Pages Required

1 page

Colors
3276b5
9bcb3c
cadf82
33a6d7

Requirements
Must have
• The ability to attract new customer and show a level of professionalism.
• You can also add a green color to represent green and environmental friendly.
Nice to have
• To give a total new fresh look for the company
Should not have
• None

```html
<!DOCTYPE html>
<html lang="en">
<head>
<meta charset="utf-8">
<title>Nexora Ledger Systems – Business Card</title>
<link href="https://fonts.googleapis.com/css2?family=Roboto:wght@300;400;500;700;900&display=swap" rel="stylesheet">
<style>
  :root {
    --stage: #302d57;
    --card: #ffffff;
    --ink: #1e1b4b;
    --ink-soft: #2b2860;
    --accent: #3b5cc4;
    --badge: #e0262b;
    --mist-1: #e6e6ee;
    --mist-2: #f3f3f7;
  }
  * { box-sizing: border-box; margin: 0; padding: 0; }
  html, body { width: 1200px; height: 900px; overflow: hidden; }
  body {
    background: radial-gradient(ellipse at 50% 40%, #3a3768 0%, var(--stage) 70%);
    font-family: "Roboto", sans-serif;
    color: var(--ink);
    position: relative;
  }
  .card {
    position: absolute;
    width: 620px;
    height: 354px;
    background: var(--card);
    border-radius: 26px;
    overflow: hidden;
    box-shadow: 0 18px 40px rgba(10, 8, 40, 0.45);
  }
  .card--front { left: 90px; top: 66px; }
  .card--back { left: 490px; top: 476px; }

  .card__mist {
    position: absolute;
    left: 0; bottom: 0;
    width: 100%; height: 46%;
    background: linear-gradient(180deg, rgba(255,255,255,0) 0%, var(--mist-2) 35%, var(--mist-1) 100%);
  }

  .brand { position: absolute; display: flex; align-items: center; gap: 14px; }
  .brand__dot {
    width: 22px; height: 22px; border-radius: 50%;
    background: var(--ink);
  }
  .brand__text { display: flex; flex-direction: column; }
  .brand__name {
    font-weight: 700;
    color: var(--ink);
    text-transform: uppercase;
    line-height: 1;
  }
  .brand__tagline {
    font-weight: 300;
    color: var(--ink-soft);
    line-height: 1;
    text-align: right;
  }

  .card--front .brand { left: 70px; top: 118px; }
  .card--front .brand__dot { width: 30px; height: 30px; }
  .card--front .brand__name { font-size: 58px; letter-spacing: 22px; }
  .card--front .brand__tagline { font-size: 13px; letter-spacing: 6px; margin-top: 10px; padding-right: 4px; }

  .partner-badge {
    position: absolute;
    right: 62px; top: 222px;
    width: 86px; height: 26px;
    background: var(--badge);
  }

  .card--back .brand { left: 36px; top: 42px; }
  .card--back .brand__dot { width: 16px; height: 16px; }
  .card--back .brand__name { font-size: 30px; letter-spacing: 11px; }
  .card--back .brand__tagline { font-size: 8px; letter-spacing: 3.5px; margin-top: 6px; }

  .contact {
    position: absolute;
    right: 36px; top: 40px;
    text-align: right;
  }
  .contact__name { font-weight: 900; font-size: 24px; letter-spacing: 0.5px; line-height: 1; }
  .contact__role { font-weight: 500; font-size: 11px; letter-spacing: 1.5px; margin-top: 4px; }
  .contact__address { font-size: 12.5px; line-height: 1.35; letter-spacing: 0.6px; margin-top: 18px; }
  .contact__lines { list-style: none; margin-top: 16px; font-size: 12.5px; letter-spacing: 0.8px; }
  .contact__lines li { display: flex; justify-content: flex-end; align-items: center; gap: 10px; height: 18px; }
  .contact__lines svg { width: 12px; height: 12px; flex: none; }
  .contact__web {
    margin-top: 20px;
    font-weight: 900; font-size: 13px; letter-spacing: 1px; line-height: 1;
  }
</style>
</head>
<body>

<section class="card card--front" aria-label="Card front">
  <div class="card__mist" role="img" aria-label="Soft pale grey flowing shapes along the lower edge"></div>
  <div class="brand">
    <span class="brand__dot"></span>
    <div class="brand__text">
      <span class="brand__name">Nexora</span>
      <span class="brand__tagline">Ledger Systems Sdn Bhd</span>
    </div>
  </div>
  <div class="partner-badge" aria-label="Partner badge"></div>
</section>

<section class="card card--back" aria-label="Card back">
  <div class="card__mist" role="img" aria-label="Soft pale grey flowing shapes along the lower edge"></div>
  <div class="brand">
    <span class="brand__dot"></span>
    <div class="brand__text">
      <span class="brand__name">Nexora</span>
      <span class="brand__tagline">Ledger Systems Sdn Bhd</span>
    </div>
  </div>

  <div class="contact">
    <p class="contact__name">ARLEN QUIST</p>
    <p class="contact__role">DIRECTOR</p>
    <p class="contact__address">Marrowgate Raya Complex<br>Serang, Indonesia</p>
    <ul class="contact__lines">
      <li>321 654 0987
        <svg viewBox="0 0 12 12" aria-hidden="true"><rect x="2.5" y="0.8" width="7" height="10.4" rx="1.2" fill="none" stroke="currentColor" stroke-width="1.4"/></svg>
      </li>
      <li>321 654 0988
        <svg viewBox="0 0 12 12" aria-hidden="true"><path d="M2 1.5h2.5l1 2.5-1.4 1a6 6 0 0 0 2.9 2.9l1-1.4 2.5 1V10a1 1 0 0 1-1 1A9 9 0 0 1 1 2.5a1 1 0 0 1 1-1z" fill="currentColor"/></svg>
      </li>
      <li>+12 343 5757
        <svg viewBox="0 0 12 12" aria-hidden="true"><rect x="3" y="0.8" width="6" height="3.5" fill="currentColor"/><rect x="0.8" y="4.8" width="10.4" height="5" rx="1" fill="currentColor"/><rect x="3" y="8.5" width="6" height="2.7" fill="#fff" stroke="currentColor" stroke-width="0.8"/></svg>
      </li>
      <li>arlen@bnlzq.com
        <svg viewBox="0 0 12 12" aria-hidden="true"><rect x="0.8" y="2.2" width="10.4" height="7.6" fill="none" stroke="currentColor" stroke-width="1.3"/><path d="M1 2.6l5 4 5-4" fill="none" stroke="currentColor" stroke-width="1.3"/></svg>
      </li>
    </ul>
    <p class="contact__web">www.bnlzq.com</p>
  </div>
</section>

</body>
</html>
```